Business Card Design with new logo

Dorian Pelleway 4172
E 118th St Brenvale, IL 62488
Cell: 217-555-0193
pellewayrestoration@mailvane.test

Classic Car Restoration Services Buy Sell Trade Consign

Dorian Pelleway 9698
Cell: 217-555-0193

```html
<!DOCTYPE html>
<html lang="en">
<head>
<meta charset="utf-8">
<title>Pelleway Restoration LLC – Business Cards</title>
<link href="https://fonts.googleapis.com/css2?family=Arimo:wght@400;700&display=swap" rel="stylesheet">
<style>
  :root {
    --backdrop: #2b2b2d;
    --card-white: #ffffff;
    --navy: #13222f;
    --red: #c0202a;
    --text-dark: #1a1f26;
  }
  * { box-sizing: border-box; margin: 0; padding: 0; }
  html, body {
    width: 1200px; height: 880px; overflow: hidden;
    background: var(--backdrop);
    font-family: "Arimo", Arial, sans-serif;
  }
  .stage {
    width: 1200px; height: 880px;
    display: flex; align-items: center; justify-content: center; gap: 60px;
  }
  .card {
    position: relative;
    width: 530px; height: 304px;
    background: var(--card-white);
    border-radius: 18px;
    overflow: hidden;
    box-shadow: 0 10px 30px rgba(0,0,0,.45);
  }
  /* Front */
  .card-front .brand {
    position: absolute; left: 0; right: 0; top: 96px;
    text-align: center;
  }
  .brand-mark {
    display: inline-block; width: 30px; height: 30px; border-radius: 50%;
    background: var(--red); vertical-align: middle; margin-right: 10px;
  }
  .brand-name {
    display: inline-block; vertical-align: middle;
    font-weight: 700; color: var(--navy);
    font-size: 30px; letter-spacing: .5px; line-height: 1.1;
    text-align: left;
  }
  .brand-name small { display: block; font-size: 15px; letter-spacing: 5px; }
  .tagline {
    position: absolute; left: 0; right: 0; top: 196px;
    text-align: center; font-weight: 700; font-size: 14.5px; color: var(--text-dark);
  }
  /* Back */
  .card-back .swoosh { position: absolute; inset: 0; }
  .card-back .brand { position: absolute; left: 34px; top: 92px; }
  .card-back .brand-name { font-size: 25px; }
  .card-back .brand-name small { font-size: 13px; letter-spacing: 4px; }
  .holder {
    position: absolute; right: 30px; top: 26px; text-align: right;
  }
  .holder-name { font-weight: 700; font-size: 16px; color: var(--text-dark); }
  .holder-role { font-size: 14px; color: var(--red); margin-top: 1px; }
  .contact {
    position: absolute; right: 26px; top: 150px;
    text-align: right; color: #fff; font-size: 13px; line-height: 1.45;
  }
  .contact-line { display: flex; justify-content: flex-end; align-items: center; gap: 6px; }
  .contact-line svg { width: 11px; height: 11px; }
</style>
</head>
<body>
<main class="stage">
  <section class="card card-front">
    <div class="brand">
      <span class="brand-mark"></span><span class="brand-name">PELLEWAY<small>RESTORATION LLC</small></span>
    </div>
    <p class="tagline">Classic Car Restoration Services Buy Sell Trade Consign</p>
  </section>

  <section class="card card-back">
    <svg class="swoosh" viewBox="0 0 530 304" preserveAspectRatio="none">
      <path d="M0 238 C130 250 245 225 280 140 C265 235 140 268 0 262 Z" fill="var(--red)"/>
      <path d="M150 304 C255 280 270 115 400 78 L530 66 L530 304 Z" fill="var(--navy)"/>
      <path d="M80 304 C220 280 230 105 385 64 C265 108 245 262 140 304 Z" fill="var(--navy)"/>
    </svg>
    <div class="brand">
      <span class="brand-mark"></span><span class="brand-name">PELLEWAY<small>RESTORATION LLC</small></span>
    </div>
    <div class="holder">
      <p class="holder-name">MARLO FENWICK</p>
      <p class="holder-role">Owner</p>
    </div>
    <div class="contact">
      <p>Dorian Pelleway 4172</p>
      <p>E 118th St Brenvale, IL 62488</p>
      <p class="contact-line">217-555-0193
        <svg viewBox="0 0 12 12"><rect x="3" y="0.5" width="6" height="11" rx="1" fill="none" stroke="#fff"/></svg></p>
      <p class="contact-line">pellewayrestoration@mailvane.test
        <svg viewBox="0 0 12 12"><rect x="0.5" y="2" width="11" height="8" fill="none" stroke="#fff"/><path d="M0.5 2 L6 7 L11.5 2" fill="none" stroke="#fff"/></svg></p>
    </div>
  </section>
</main>
</body>
</html>
```